2022 Spring Circle of Patrons (art gallery annual report)

6X9, 16-page brochure that serves both as an annual report for the previous year and gets mailed for an ask for donations. This must be done in InDesign and I will provide a template. I am also sending PDFs for the previous two years. Last year was pink and black, but I have recolored the logo purple this year.. so am open to whatever colors. I used last year's template to put in the new info. The theme for this year is Amazing - last year was Thriving. The font I chose for the front I do not want to use.. its just an example. All three pictures on the front don't have to be used.. just ideas.
Updates

I put three photos on the front page. It isn't necessary to use all of them, I thought there might be something there to use as part of the design

The current information is in the InDesign file, Calatalog Design.indd with the to Links Folders attached.

Target Market(s)

Donors

Industry/Entity Type

Art

Font styles to use
Sans Serif

Requirements
Must have
• InDesign
Nice to have
• A new look! Something different than 2021 an 2020 (PDFs included)

```html
<!DOCTYPE html>
<html lang="en">
<head>
<meta charset="utf-8">
<title>Satellites</title>
<link href="https://fonts.googleapis.com/css2?family=Oswald:wght@500&family=Open+Sans:wght@400&display=swap" rel="stylesheet">
<style>
  :root {
    --accent-orange: #f2722b;
    --panel-shade: rgba(38, 32, 28, 0.62);
    --body-text: #f7f3ee;
    --wall-light: #d9c6a8;
    --wall-warm: #9a6a47;
    --room-mid: #6f5a44;
    --floor-dark: #4a3a30;
  }
  html, body {
    margin: 0;
    padding: 0;
    width: 1200px;
    height: 800px;
    overflow: hidden;
  }
  .page {
    position: relative;
    width: 1200px;
    height: 800px;
    overflow: hidden;
    font-family: "Open Sans", Arial, sans-serif;
  }
  .page-photo {
    position: absolute;
    inset: 0;
    background:
      linear-gradient(180deg, rgba(240,236,230,0.85) 0%, rgba(240,236,230,0) 22%),
      linear-gradient(90deg, var(--wall-light) 0%, var(--wall-light) 22%, var(--wall-warm) 24%, var(--wall-warm) 50%, #b8a68a 52%, #9e9a82 80%, #b88a5c 100%),
      var(--room-mid);
  }
  .page-photo::after {
    content: "";
    position: absolute;
    left: 0; right: 0; bottom: 0;
    height: 26%;
    background: linear-gradient(180deg, rgba(74,58,48,0.2) 0%, var(--floor-dark) 100%);
  }
  .section-title {
    position: absolute;
    left: 234px;
    top: 140px;
    margin: 0;
    font-family: "Oswald", "Arial Narrow", sans-serif;
    font-weight: 500;
    font-size: 66px;
    line-height: 1;
    letter-spacing: -0.5px;
    color: var(--accent-orange);
    text-transform: uppercase;
  }
  .story-panel {
    position: absolute;
    left: 236px;
    top: 242px;
    width: 727px;
    height: 491px;
    background: var(--panel-shade);
    box-sizing: border-box;
    padding: 42px 40px 0 43px;
  }
  .story-panel p {
    margin: 0 0 17px;
    color: var(--body-text);
    font-size: 18px;
    line-height: 24px;
    max-width: 640px;
  }
  .story-panel p.closing { margin-top: -17px; }
</style>
</head>
<body>
  <main class="page">
    <div class="page-photo" role="img" aria-label="Photo of a hotel lobby dining room with framed landscape paintings on the walls, wooden tables, black chairs and a sliding barn door"></div>

    <h1 class="section-title">Satellites</h1>

    <section class="story-panel">
      <p>Our continued partnerships with The Meridian Concert Hall Gallery Café and the beautiful Hotel Larkspur have enabled us to showcase even more artists from the Cedar Basin.</p>
      <p>Guests for Hollis Art Gallery events at The Meridian Concert Hall were offered special entry to live music performances–a treat for both the eyes and ears, all in one location. This past year, guests tasted wine, enjoyed treats from the Meridian Café, and mingled with talented local artists including Renata Lyle, Colette Varga, Peter Hale, and Miriam Ostrander Pike</p>
      <p>Visitors to the Hotel Larkspur don’t have to go far to get a sense of the local art scene. Rows of orchards and watercolor landscapes of the Basin’s shrub-steppe by the likes of local legendary artists Glen Harrow, R.T. Lowell, and Edwin Van Holt grace the walls of the main lobby.</p>
      <p class="closing">And the best part? The art is all available for purchase.</p>
    </section>
  </main>
</body>
</html>
```